High-end residential home builder needs a business card design

We need a new business card design for a small residential construction company based in Boise, Idaho. We specialize in building custom high-end homes and remodels, with a focus on great design and craftsmanship.

We would like to use our current logo, but open to new color suggestions.
Just looking for a clean, sharp, modern design that looks high-end.

Target Market(s)

Upscale clientele

Industry/Entity Type

Contractor

Contact Information for Business Card

Company: Stonehaven Custom Builders
Name: Colin Marsh
Phone number: 208 637 4120
Email: ColinMarshSCB@quillpost.net
Website: Stonehavencustombuilders.com

Font styles to use
Serif
Sans Serif

Requirements
Must have
• Company Logo
Company name
My name
My phone number
My email
Company website
Nice to have
• I have attached a few photos of cards that I really like.

```html
<!DOCTYPE html>
<html lang="en">
<head>
<meta charset="utf-8">
<title>Stonehaven Custom Builders – Business Card</title>
<link href="https://fonts.googleapis.com/css2?family=Michroma&family=Open+Sans:wght@400;600&family=Raleway:wght@600&display=swap" rel="stylesheet">
<style>
  :root {
    --backdrop: #5b5b5b;
    --card: #ffffff;
    --brown: #3d2f29;
    --orange: #e08f36;
    --ink: #333333;
  }
  * { box-sizing: border-box; margin: 0; padding: 0; }
  html, body { width: 1200px; height: 1000px; overflow: hidden; }
  body { background: var(--backdrop); position: relative; font-family: "Open Sans", sans-serif; color: var(--ink); }

  .card { position: absolute; width: 542px; height: 316px; background: var(--card); overflow: hidden; }
  .card--front { left: 229px; top: 170px; }
  .card--back { left: 392px; top: 516px; }

  .holder { position: absolute; left: 25px; top: 124px; }
  .holder__name { font-family: "Michroma", sans-serif; font-size: 12.5px; letter-spacing: 2px; color: var(--orange); line-height: 1; }
  .holder__title { font-size: 8.5px; color: var(--ink); margin-top: 2px; }

  .contacts { position: absolute; left: 25px; top: 181px; list-style: none; }
  .contacts li { display: flex; align-items: center; height: 19px; margin-bottom: 3.5px; font-size: 11px; }
  .contacts svg { width: 19px; height: 19px; margin-right: 7px; flex: none; }

  .address { position: absolute; left: 392px; top: 233px; font-size: 9px; line-height: 13px; color: var(--ink); }

  .brand { position: absolute; display: flex; align-items: center; }
  .brand__mark { border: 2.5px solid var(--brown); border-radius: 50%; flex: none; }
  .brand__name { font-family: "Raleway", sans-serif; font-weight: 600; color: var(--brown); text-transform: uppercase; line-height: 1; }
  .brand__line { display: block; }

  .card--front .brand { left: 252px; top: 96px; }
  .card--front .brand__mark { width: 66px; height: 66px; margin-right: 18px; }
  .card--front .brand__line--main { font-size: 17px; letter-spacing: 6px; }
  .card--front .brand__line--sub { font-size: 10px; letter-spacing: 4.5px; margin-top: 12px; padding-left: 13px; }

  .card--back .brand { left: 110px; top: 110px; }
  .card--back .brand__mark { width: 86px; height: 86px; margin-right: 22px; }
  .card--back .brand__line--main { font-size: 21px; letter-spacing: 7.5px; }
  .card--back .brand__line--sub { font-size: 13px; letter-spacing: 5.5px; margin-top: 16px; padding-left: 16px; }

  .band { position: absolute; left: 0; bottom: 0; width: 542px; height: 16px; }
</style>
</head>
<body>

<section class="card card--front" aria-label="Business card front">
  <div class="holder">
    <p class="holder__name">COLIN MARSH</p>
    <p class="holder__title">CEO/Managing Director</p>
  </div>

  <ul class="contacts">
    <li>
      <svg viewBox="0 0 20 20" aria-hidden="true"><circle cx="10" cy="10" r="9" fill="none" stroke="var(--orange)" stroke-width="1.2"/><rect x="7" y="4.5" width="6" height="11" rx="1" fill="none" stroke="var(--orange)" stroke-width="1.2"/><circle cx="10" cy="13.6" r=".7" fill="var(--orange)"/></svg>
      208 637 4120
    </li>
    <li>
      <svg viewBox="0 0 20 20" aria-hidden="true"><circle cx="10" cy="10" r="9" fill="none" stroke="var(--orange)" stroke-width="1.2"/><path d="M5 10 L10 5.5 L15 10 L13.5 10 L13.5 14.5 L6.5 14.5 L6.5 10 Z" fill="var(--orange)"/></svg>
      208 637 4120
    </li>
    <li>
      <svg viewBox="0 0 20 20" aria-hidden="true"><circle cx="10" cy="10" r="9" fill="none" stroke="var(--orange)" stroke-width="1.2"/><rect x="5" y="6.5" width="10" height="7" fill="var(--orange)"/><path d="M5 6.5 L10 10.5 L15 6.5" fill="none" stroke="#fff" stroke-width="1"/></svg>
      ColinMarshSCB@quillpost.net
    </li>
    <li>
      <svg viewBox="0 0 20 20" aria-hidden="true"><circle cx="10" cy="10" r="9" fill="none" stroke="var(--orange)" stroke-width="1.2"/><circle cx="10" cy="10" r="5.5" fill="none" stroke="var(--orange)" stroke-width="1"/><ellipse cx="10" cy="10" rx="2.4" ry="5.5" fill="none" stroke="var(--orange)" stroke-width="1"/><path d="M4.5 10 H15.5 M5.3 7.3 H14.7 M5.3 12.7 H14.7" stroke="var(--orange)" stroke-width="1"/></svg>
      Stonehavencustombuilders.com
    </li>
  </ul>

  <div class="brand">
    <span class="brand__mark" aria-hidden="true"></span>
    <p class="brand__name">
      <span class="brand__line brand__line--main">Stonehaven</span>
      <span class="brand__line brand__line--sub">Custom Builders</span>
    </p>
  </div>

  <address class="address" style="font-style:normal">
    418 Harlow Avenue NW Suite<br>
    210 Boise ID 83702
  </address>

  <svg class="band" viewBox="0 0 542 16" preserveAspectRatio="none" aria-hidden="true">
    <polygon points="0,0 276,0 263,16 0,16" fill="var(--brown)"/>
    <polygon points="279,0 542,0 542,16 266,16" fill="var(--orange)"/>
  </svg>
</section>

<section class="card card--back" aria-label="Business card back">
  <div class="brand">
    <span class="brand__mark" aria-hidden="true"></span>
    <p class="brand__name">
      <span class="brand__line brand__line--main">Stonehaven</span>
      <span class="brand__line brand__line--sub">Custom Builders</span>
    </p>
  </div>
</section>

</body>
</html>
```